Real estate investor, needing a business card that communicates warmth, integrity, empathy.

I have a logo that can be manipulated to align with the message - "Serving your home selling needs." Want it to stand out from typical real estate investor cards, and make distressed home sellers feel a connection with me. Should communicate warmth, integrity, empathy, and trustworthiness.

Target Market(s)

Distressed home owners who need to sell their homes, not using realtors.

Contact Information for Business Card

Glossy front and matte back, with a small box that is labelled "notes." I like darker blues and blacks together, but doesn't have to be, as long as it communicates trustworthiness, and a strong call to action.

Other font styles liked:
• see "must haves" above, but willing to review whatever comes my way.

Requirements
Must have
• The fonts on my logo are Aviano, Lusitana, and Marcellus. We don't have to use those, but I favor them.

```html
<!DOCTYPE html>
<html lang="en">
<head>
<meta charset="utf-8">
<title>Ridgeline Home Partners – Business Card</title>
<link rel="stylesheet" href="https://fonts.googleapis.com/css2?family=Lusitana:wght@400;700&family=Marcellus&display=swap">
<style>
  :root {
    --stage: #151515;
    --ink-black: #050508;
    --navy: #262470;
    --bronze: #b27a4a;
    --white: #ffffff;
    --paper: #ffffff;
  }
  * { margin: 0; padding: 0; box-sizing: border-box; }
  html, body { width: 1200px; height: 1200px; overflow: hidden; background: var(--stage); }
  body { position: relative; font-family: "Lusitana", Georgia, serif; color: var(--white); }

  .card {
    position: absolute;
    left: 150px;
    width: 900px;
    height: 527px;
    background: linear-gradient(120deg, var(--ink-black) 0%, #0b0b1c 30%, #1b1a52 62%, var(--navy) 100%);
    box-shadow: 0 14px 40px rgba(0,0,0,.6);
    overflow: hidden;
  }
  .card--back { top: 40px; }
  .card--front { top: 633px; }

  /* Back side */
  .services { position: absolute; left: 58px; top: 42px; }
  .services__title {
    font-family: "Marcellus", Georgia, serif;
    color: var(--bronze);
    font-size: 21px;
    letter-spacing: 1px;
    margin-bottom: 4px;
  }
  .services__list { list-style: none; }
  .services__item {
    display: flex; align-items: center; gap: 10px;
    font-size: 21px; line-height: 29px;
  }
  .services__icon { width: 20px; height: 14px; flex: none; }

  .notes { position: absolute; left: 50px; right: 50px; top: 385px; }
  .notes__label { font-family: "Marcellus", Georgia, serif; font-size: 16px; letter-spacing: .5px; margin-bottom: 6px; }
  .notes__box { height: 78px; background: var(--paper); }

  .brand {
    position: absolute;
    text-align: center;
  }
  .brand--back { left: 440px; top: 120px; width: 420px; }
  .brand--front { left: 30px; top: 150px; width: 400px; }
  .brand__mark { width: 14px; height: 14px; background: var(--bronze); display: block; margin: 0 auto 16px; }
  .brand__name {
    font-family: "Marcellus", Georgia, serif;
    font-size: 50px; line-height: 1.05;
    color: var(--white);
    letter-spacing: 2px;
  }
  .brand__tagline {
    margin-top: 22px;
    font-family: "Marcellus", Georgia, serif;
    font-size: 15px; letter-spacing: 1px;
    color: var(--white);
  }

  /* Front side */
  .divider {
    position: absolute; left: 462px; top: 90px;
    width: 2px; height: 350px;
    background: linear-gradient(var(--bronze) 0%, var(--bronze) 40%, var(--white) 40%, var(--white) 100%);
  }
  .contact { position: absolute; left: 505px; top: 90px; }
  .contact__name {
    font-family: "Marcellus", Georgia, serif;
    font-size: 40px; letter-spacing: 1px; line-height: 1;
  }
  .contact__role {
    font-family: "Marcellus", Georgia, serif;
    font-size: 22px; letter-spacing: 1px;
    color: var(--bronze); margin-top: 2px; margin-bottom: 22px;
  }
  .contact__list { list-style: none; }
  .contact__row { display: flex; align-items: flex-start; gap: 14px; font-size: 22px; line-height: 31px; }
  .contact__row--address { margin-top: 16px; line-height: 30px; }
  .contact__icon { width: 18px; height: 18px; flex: none; margin-top: 6px; fill: var(--bronze); }
</style>
</head>
<body>

<section class="card card--back" aria-label="Card back">
  <div class="services">
    <h2 class="services__title">HELPING WITH</h2>
    <ul class="services__list">
      <li class="services__item"><svg class="services__icon" viewBox="0 0 20 14"><path d="M1 13 L10 2 L19 13" fill="none" stroke="#b27a4a" stroke-width="3"/></svg>Sellers needing cash</li>
      <li class="services__item"><svg class="services__icon" viewBox="0 0 20 14"><path d="M1 13 L10 2 L19 13" fill="none" stroke="#b27a4a" stroke-width="3"/></svg>Probate situations</li>
      <li class="services__item"><svg class="services__icon" viewBox="0 0 20 14"><path d="M1 13 L10 2 L19 13" fill="none" stroke="#b27a4a" stroke-width="3"/></svg>Foreclosure situations</li>
      <li class="services__item"><svg class="services__icon" viewBox="0 0 20 14"><path d="M1 13 L10 2 L19 13" fill="none" stroke="#b27a4a" stroke-width="3"/></svg>Inheritance</li>
      <li class="services__item"><svg class="services__icon" viewBox="0 0 20 14"><path d="M1 13 L10 2 L19 13" fill="none" stroke="#b27a4a" stroke-width="3"/></svg>Vacant properties</li>
      <li class="services__item"><svg class="services__icon" viewBox="0 0 20 14"><path d="M1 13 L10 2 L19 13" fill="none" stroke="#b27a4a" stroke-width="3"/></svg>Divorce sales</li>
      <li class="services__item"><svg class="services__icon" viewBox="0 0 20 14"><path d="M1 13 L10 2 L19 13" fill="none" stroke="#b27a4a" stroke-width="3"/></svg>Relocating / Downsizing</li>
      <li class="services__item"><svg class="services__icon" viewBox="0 0 20 14"><path d="M1 13 L10 2 L19 13" fill="none" stroke="#b27a4a" stroke-width="3"/></svg>Estate sales</li>
      <li class="services__item"><svg class="services__icon" viewBox="0 0 20 14"><path d="M1 13 L10 2 L19 13" fill="none" stroke="#b27a4a" stroke-width="3"/></svg>Need of repairs</li>
      <li class="services__item"><svg class="services__icon" viewBox="0 0 20 14"><path d="M1 13 L10 2 L19 13" fill="none" stroke="#b27a4a" stroke-width="3"/></svg>Owe taxes</li>
    </ul>
  </div>

  <div class="brand brand--back">
    <span class="brand__mark"></span>
    <p class="brand__name">Ridgeline<br>Home Partners</p>
    <p class="brand__tagline">SERVING YOUR HOME SELLING NEEDS</p>
  </div>

  <div class="notes">
    <p class="notes__label">NOTES</p>
    <div class="notes__box"></div>
  </div>
</section>

<section class="card card--front" aria-label="Card front">
  <div class="brand brand--front">
    <span class="brand__mark"></span>
    <p class="brand__name">Ridgeline<br>Home Partners</p>
    <p class="brand__tagline">SERVING YOUR HOME SELLING NEEDS</p>
  </div>

  <div class="divider"></div>

  <div class="contact">
    <h1 class="contact__name">DANIEL REYES</h1>
    <p class="contact__role">MANAGING PARTNER</p>
    <ul class="contact__list">
      <li class="contact__row">
        <svg class="contact__icon" viewBox="0 0 24 24"><path d="M6.6 10.8c1.4 2.8 3.8 5.1 6.6 6.6l2.2-2.2c.3-.3.7-.4 1-.2 1.1.4 2.3.6 3.6.6.6 0 1 .4 1 1V20c0 .6-.4 1-1 1C10.6 21 3 13.4 3 4c0-.6.4-1 1-1h3.5c.6 0 1 .4 1 1 0 1.3.2 2.5.6 3.6.1.3 0 .7-.2 1z"/></svg>
        555-014-2738
      </li>
      <li class="contact__row">
        <svg class="contact__icon" viewBox="0 0 24 24"><path d="M6 2h12v5H6z M3 8h18a1 1 0 0 1 1 1v8h-4v-3H6v3H2V9a1 1 0 0 1 1-1z M7 15h10v7H7z"/></svg>
        555-014-2738
      </li>
      <li class="contact__row">
        <svg class="contact__icon" viewBox="0 0 24 24"><path d="M2 5h20v14H2z" fill="#b27a4a"/><path d="M2 5l10 8 10-8" fill="none" stroke="#1a1a4a" stroke-width="2"/></svg>
        daniel@ridgelinehome.com
      </li>
      <li class="contact__row">
        <svg class="contact__icon" viewBox="0 0 24 24"><g fill="none" stroke="#b27a4a" stroke-width="2"><circle cx="12" cy="12" r="10"/><ellipse cx="12" cy="12" rx="4" ry="10"/><path d="M2 12h20M4 7h16M4 17h16"/></g></svg>
        www.ridgelinehome.com
      </li>
      <li class="contact__row contact__row--address">
        <svg class="contact__icon" viewBox="0 0 24 24"><path d="M12 2a7 7 0 0 0-7 7c0 5 7 13 7 13s7-8 7-13a7 7 0 0 0-7-7zm0 9.5a2.5 2.5 0 1 1 0-5 2.5 2.5 0 0 1 0 5z"/></svg>
        <span>418 Alder Street NE<br>Suite 210, Lakeview<br>MI 49512</span>
      </li>
    </ul>
  </div>
</section>

</body>
</html>
```